Create the ONLY Supplement line for Male Entrepreneurs! (Verdant Crest MD)

I need a label designed for a new supplement brand that I am launching.

There are five products so need a design that I can simply change the wording for each individual product

The brand name is called verdant crest MD. The focus is male entrepreneurial health.

Target audience is men 35 to 55.

Concepts: the healthier you are in body the more money you will make in business.

Concept to copy: I want to make a clean minimalistic label mimicking Halvorsen MD (google it and you'll see what I mean)
Updates

Target Market(s)

male entrepreneurs 35-55

Industry/Entity Type

Health Supplement

Colors

Designer to choose colors to be used in the design.

Requirements
Must have
• Modern classy design, similar to Halvorsen MD.
Nice to have
• Highlight that the supplement is Doctor Approved.
Should not have
• No loud colors. Present it as high class.

```html
<!DOCTYPE html>
<html lang="en">
<head>
<meta charset="utf-8">
<title>Verdant Crest MD – Supplement Labels</title>
<link rel="stylesheet" href="https://fonts.googleapis.com/css2?family=Cormorant+Garamond:wght@500&family=Montserrat:wght@400;500&display=swap">
<style>
  :root {
    --page: #ffffff;
    --ink: #8a8b8e;
    --ink-soft: #9a9b9e;
    --rule: #c2c3c5;
    --label-white: #f5f5f2;
    --label-white-edge: #e3e3e0;
    --label-blue: #d4e0e9;
    --label-blue-edge: #c6d3dd;
  }
  * { box-sizing: border-box; margin: 0; padding: 0; }
  html, body {
    width: 1200px;
    height: 1200px;
    overflow: hidden;
    background: var(--page);
  }
  .canvas {
    position: relative;
    width: 1200px;
    height: 1200px;
  }

  /* Brand lockup */
  .brand {
    position: absolute;
    top: 160px;
    left: 0;
    width: 1200px;
    display: flex;
    flex-direction: column;
    align-items: center;
  }
  .brand-name {
    display: flex;
    align-items: center;
    gap: 20px;
    font-family: "Montserrat", sans-serif;
    font-weight: 500;
    font-size: 42px;
    line-height: 1;
    letter-spacing: 6px;
    text-transform: uppercase;
    color: var(--ink);
  }
  .brand-mark {
    width: 22px;
    height: 22px;
    background: var(--ink);
    flex: none;
  }
  .brand-tagline {
    margin-top: 38px;
    font-family: "Montserrat", sans-serif;
    font-weight: 400;
    font-size: 29px;
    color: var(--ink-soft);
    letter-spacing: 0.3px;
  }

  /* Labels */
  .label {
    position: absolute;
    border: 1px solid var(--label-white-edge);
  }
  .label--omega {
    left: 240px;
    top: 640px;
    width: 340px;
    height: 396px;
    background: var(--label-white);
  }
  .label--multi {
    left: 600px;
    top: 592px;
    width: 336px;
    height: 380px;
    background: var(--label-blue);
    border-color: var(--label-blue-edge);
  }

  .label-brand {
    position: absolute;
    left: 28px;
    right: 24px;
    top: 84px;
  }
  .label-name {
    display: flex;
    align-items: center;
    gap: 10px;
    font-family: "Montserrat", sans-serif;
    font-weight: 500;
    font-size: 17px;
    line-height: 1;
    letter-spacing: 2.5px;
    text-transform: uppercase;
    color: var(--ink);
  }
  .label-name .brand-mark { width: 11px; height: 11px; }
  .label-tagline {
    margin-top: 14px;
    font-family: "Montserrat", sans-serif;
    font-size: 15px;
    color: var(--ink-soft);
  }

  .product {
    position: absolute;
    left: 28px;
    right: 24px;
  }
  .label--omega .product { top: 258px; }
  .label--multi .product { top: 248px; }
  .product-name {
    font-family: "Cormorant Garamond", serif;
    font-weight: 500;
    font-size: 33px;
    line-height: 1;
    color: var(--ink-soft);
  }
  .product-rule {
    height: 1.5px;
    margin: 6px 0;
    background: var(--rule);
  }
  .product-type,
  .product-count {
    font-family: "Montserrat", sans-serif;
    font-size: 15.5px;
    line-height: 1.2;
    color: var(--ink);
  }
</style>
</head>
<body>
<main class="canvas">

  <header class="brand">
    <div class="brand-name"><span class="brand-mark"></span>Verdant Crest MD</div>
    <p class="brand-tagline">male entrepreneurial health</p>
  </header>

  <article class="label label--omega">
    <div class="label-brand">
      <div class="label-name"><span class="brand-mark"></span>Verdant Crest MD</div>
      <p class="label-tagline">male entrepreneurial health</p>
    </div>
    <div class="product">
      <h2 class="product-name">Omega 3</h2>
      <div class="product-rule"></div>
      <p class="product-type">Dietary Supplement</p>
      <div class="product-rule"></div>
      <p class="product-count">90 softgel</p>
    </div>
  </article>

  <article class="label label--multi">
    <div class="label-brand">
      <div class="label-name"><span class="brand-mark"></span>Verdant Crest MD</div>
      <p class="label-tagline">male entrepreneurial health</p>
    </div>
    <div class="product">
      <h2 class="product-name">Multivit Male</h2>
      <div class="product-rule"></div>
      <p class="product-type">Dietary Supplement</p>
      <div class="product-rule"></div>
      <p class="product-count">90 softgel</p>
    </div>
  </article>

</main>
</body>
</html>
```